Lionel Arbusto and Dwight Halvorsen Advertisement

We would like an ad that conveys understated elegance. We are a company that purchases estate jewelry watches and diamonds. We care to a wealthy, upscale clientele.

Target Market(s)

Wealthy upscale.

Industry/Entity Type

It Company

Requirements
Must have
• Elegant Design. Crisp Clean. Attached a doc of how the ad should be arranged.

```html
<!DOCTYPE html>
<html lang="en">
<head>
<meta charset="utf-8">
<title>Lionel Arbusto &amp; Dwight Halvorsen — Ad Sizes</title>
<link href="https://fonts.googleapis.com/css2?family=Cinzel:wght@400&family=EB+Garamond:wght@400&family=Arimo:wght@400;700&display=swap" rel="stylesheet">
<style>
  :root {
    --page: #ffffff;
    --ad-edge: #9e9e9e;
    --ad-mid: #d9d9d9;
    --ad-light: #e4e4e4;
    --ink-white: #ffffff;
    --ink-dark: #3b3b3b;
    --ink-label: #6e6e6e;
    --gem-light: #f4f4f4;
    --gem-mid: #c9c9c9;
    --gem-dark: #8a8a8a;
  }
  * { margin: 0; padding: 0; box-sizing: border-box; }
  html, body { width: 833px; height: 1200px; overflow: hidden; background: var(--page); }
  .sheet { position: relative; width: 833px; height: 1200px; }

  .ad {
    position: absolute;
    overflow: hidden;
    background: radial-gradient(ellipse at 50% 45%, var(--ad-light) 0%, var(--ad-mid) 40%, var(--ad-edge) 100%);
    color: var(--ink-white);
    text-align: center;
  }
  .ad--vertical { left: 216px; top: 36px; width: 408px; height: 626px; }
  .ad--horizontal { left: 50px; top: 711px; width: 575px; height: 405px; }

  .headline {
    position: absolute;
    font-family: "Cinzel", serif;
    font-weight: 400;
    color: var(--ink-white);
    letter-spacing: 0.02em;
  }
  .ad--vertical .headline { left: 0; right: 0; top: 54px; font-size: 45px; line-height: 44px; }
  .ad--horizontal .headline { left: 304px; width: 206px; top: 58px; font-size: 50px; line-height: 48px; }

  .gem {
    position: absolute;
    background: linear-gradient(135deg, var(--gem-light) 0%, var(--gem-mid) 45%, var(--gem-light) 60%, var(--gem-dark) 100%);
    clip-path: polygon(14% 0, 86% 0, 100% 14%, 100% 86%, 86% 100%, 14% 100%, 0 86%, 0 14%);
  }
  .ad--vertical .gem { left: 104px; top: 178px; width: 214px; height: 190px; transform: rotate(7deg); }
  .ad--horizontal .gem { left: 30px; top: 40px; width: 240px; height: 240px; transform: rotate(7deg); }

  .brand-name {
    position: absolute;
    font-family: "Cinzel", serif;
    font-weight: 400;
    font-size: 14px;
    letter-spacing: 0.04em;
    white-space: nowrap;
    color: var(--ink-dark);
    text-align: center;
  }
  .ad--vertical .brand-name { left: 0; right: 0; top: 464px; }
  .ad--horizontal .brand-name { left: 270px; width: 268px; top: 302px; }

  .promise {
    position: absolute;
    left: 0; right: 0;
    font-family: "EB Garamond", serif;
    letter-spacing: 0.3em;
    color: var(--ink-white);
  }
  .ad--vertical .promise { top: 514px; font-size: 17px; line-height: 24px; }
  .ad--horizontal .promise { top: 342px; font-size: 19px; line-height: 22px; letter-spacing: 0.34em; }

  .contact {
    position: absolute;
    left: 0; right: 0;
    font-family: "EB Garamond", serif;
    font-size: 11.5px;
    line-height: 14px;
    color: var(--ink-dark);
  }
  .ad--vertical .contact { top: 573px; }
  .ad--horizontal .contact { top: 374px; font-size: 11px; }
  .contact span + span { margin-left: 6px; }

  .size-label { position: absolute; font-family: "Arimo", sans-serif; color: var(--ink-label); }
  .size-label__title { font-weight: 700; font-size: 23px; line-height: 25px; }
  .size-label__dims { font-size: 12px; margin-top: 8px; }
  .size-label--vertical { left: 56px; top: 589px; }
  .size-label--horizontal { left: 639px; top: 1045px; }
</style>
</head>
<body>
<div class="sheet">

  <section class="ad ad--vertical">
    <h1 class="headline">READY<br>TO SELL?</h1>
    <div class="gem" role="img" aria-label="Photograph of a large emerald-cut diamond"></div>
    <p class="brand-name">LIONEL ARBUSTO &amp; DWIGHT HALVORSEN</p>
    <p class="promise">Utmost Discretion<br>By Appointment</p>
    <p class="contact">Casa Serena, 118-B Laurel Avenue, Palm Harbor, FL 33490<br>desk@arbustohalvorsen.com&nbsp; 561.555.0147</p>
  </section>

  <div class="size-label size-label--vertical">
    <div class="size-label__title">Half-page<br>vertical</div>
    <div class="size-label__dims">(4-5/8” W X 7-1/2” H)</div>
  </div>

  <section class="ad ad--horizontal">
    <div class="gem" role="img" aria-label="Photograph of a large emerald-cut diamond"></div>
    <h1 class="headline">READY<br>TO<br>SELL?</h1>
    <p class="brand-name">LIONEL ARBUSTO &amp; DWIGHT HALVORSEN</p>
    <p class="promise">Utmost Discretion By Appointment</p>
    <p class="contact"><span>Casa Serena, 118-B Laurel Avenue, Palm Harbor, FL 33490</span><span>desk@arbustohalvorsen.com</span><span>561.555.0147</span></p>
  </section>

  <div class="size-label size-label--horizontal">
    <div class="size-label__title">Half-page<br>horizontal</div>
    <div class="size-label__dims">(6-7/8” W X&nbsp; 4-7/8” H)</div>
  </div>

</div>
</body>
</html>
```